Buch-/E-Book-Cover für Sachbuch über Hunderasse
Zielgruppe
Ich benötige ein Buch-Cover im DIN A5 Format für ein anspruchsvolles Sachbuch, das die rassetypischen Krankheiten der Hunderasse Rhodesian Ridgeback thematisiert. Die Zielgruppe sind Züchter, Tierärzte und Liebhaber der Rasse.
Aufgabenstellung
Den größten Raum sollte ein Foto der Rasse einnehmen. Das Foto würde ich stellen, im Entwurf kann also ein Beispielfoto verwendet werden. Da das Buch der Auftakt zu einer Reihe ist, sollte das Design einen hohen Wiedererkennungswert haben und in erster Linie seriös wirken. Das Foto, der Rassename und die verwendeten Farben sollten leicht austauschbar sein. Sowohl der Titel als auch der Untertitel sind recht lang. Der Arbeitstitel lautet: Stille Pfade im Nebel der Ostseeküste, Untertitel: Geschichten von Fischern und Leuchttürmen.

```html
<!DOCTYPE html>
<html lang="de">
<head>
<meta charset="utf-8">
<title>Stille Pfade im Nebel der Ostseeküste – Cover</title>
<link rel="stylesheet" href="https://fonts.googleapis.com/css2?family=Catamaran:wght@300;400&display=swap">
<style>
  :root {
    --cover-rust: #9b4a2e;
    --spine-line: #b2664a;
    --accent-orange: #e8501a;
    --text-light: #ffffff;
    --band-dark: rgba(52, 36, 31, 0.72);
    --photo-bark: #2e2822;
    --photo-sage: #5b655e;
    --photo-mist: #6d766f;
    --photo-warm: #a5583a;
    --photo-warm-deep: #7a3d27;
  }
  * { margin: 0; padding: 0; box-sizing: border-box; }
  html, body { width: 1200px; height: 635px; overflow: hidden; background: #ffffff; }
  .cover {
    position: relative; width: 1200px; height: 635px;
    font-family: "Catamaran", "Segoe UI", sans-serif; font-weight: 300;
    color: var(--text-light);
  }
  .back {
    position: absolute; left: 0; top: 0; width: 581px; height: 635px;
    background: var(--cover-rust);
  }
  .back-title {
    position: absolute; left: 130px; top: 80px;
    font-size: 33px; line-height: 38px; font-weight: 300; letter-spacing: -0.2px;
  }
  .back-subtitle {
    position: absolute; left: 131px; top: 164px;
    font-size: 16.5px; font-weight: 300;
  }
  .back-blurb {
    position: absolute; left: 130px; top: 215px; width: 285px;
    font-size: 14.6px; line-height: 17.6px; font-weight: 300;
  }
  .isbn {
    position: absolute; left: 140px; top: 578px;
    font-size: 11px; font-weight: 300;
  }
  .spine {
    position: absolute; left: 581px; top: 0; width: 22px; height: 635px;
    background: var(--cover-rust);
    border-left: 1px solid var(--spine-line);
    border-right: 1.5px solid var(--accent-orange);
  }
  .spine-text {
    position: absolute; left: 50%; white-space: nowrap;
    font-size: 11.4px; font-weight: 300;
    transform-origin: left center;
  }
  .spine-title { top: 602px; transform: translateX(-6px) rotate(-90deg); }
  .spine-subtitle { top: 303px; transform: translateX(-6px) rotate(-90deg); }
  .front {
    position: absolute; left: 603px; top: 0; width: 597px; height: 635px;
    overflow: hidden;
  }
  .front-photo {
    position: absolute; inset: 0;
    background:
      radial-gradient(ellipse 30% 40% at 58% 42%, var(--photo-warm) 0%, #93492f 45%, rgba(122,61,39,0.6) 75%, transparent 100%),
      radial-gradient(ellipse 26% 55% at 55% 18%, rgba(140,70,45,0.85) 0%, transparent 100%),
      linear-gradient(100deg, var(--photo-bark) 0%, #3d352e 9%, var(--photo-sage) 24%, var(--photo-mist) 50%, var(--photo-sage) 76%, #3a3630 90%, var(--photo-bark) 100%),
      linear-gradient(180deg, var(--photo-mist) 0%, var(--photo-bark) 100%);
    background-blend-mode: normal, normal, normal, multiply;
  }
  .title-band {
    position: absolute; left: 57px; top: 427px; width: 540px; height: 175px;
    background: var(--band-dark);
  }
  .title-bar {
    position: absolute; left: 57px; top: 430px; width: 10px; height: 172px;
    background: var(--accent-orange);
  }
  .front-title {
    position: absolute; left: 94px; top: 446px;
    font-size: 39px; line-height: 48px; font-weight: 300; letter-spacing: -0.3px;
  }
  .front-subtitle {
    position: absolute; left: 97px; top: 552px;
    font-size: 21px; font-weight: 300; color: var(--accent-orange);
  }
</style>
</head>
<body>
<div class="cover">
  <section class="back">
    <h1 class="back-title">Stille Pfade im Nebel<br>der Ostseeküste</h1>
    <p class="back-subtitle">Geschichten von Fischern und Leuchttürmen</p>
    <p class="back-blurb">Den größten Raum sollte ein Foto der Rasse einnehmen. Das Foto würde ich stellen, im Entwurf kann also ein Beispielfoto verwendet werden. Da das Buch der Auftakt zu einer Reihe ist, sollte das Design einen hohen Wiedererkennungswert haben und in erster Linie seriös wirken. Das Foto, der Rassename und die verwendeten Farben sollten leicht austauschbar sein. Sowohl der Titel als auch der Untertitel sind recht lang. Der Arbeitstitel lautet: Stille Pfade im Nebel der Ostseeküste, Untertitel: Geschichten von Fischern und Leuchttürmen.</p>
    <p class="isbn">ISBN 1234567889</p>
  </section>

  <section class="spine">
    <span class="spine-text spine-title">Stille Pfade im Nebel der Ostseeküste</span>
    <span class="spine-text spine-subtitle">Geschichten von Fischern und Leuchttürmen</span>
  </section>

  <section class="front">
    <div class="front-photo" role="img" aria-label="Titelfoto: junger rotbrauner Hund läuft zwischen dunklen Baumstämmen vor unscharfem grüngrauem Hintergrund"></div>
    <div class="title-band"></div>
    <div class="title-bar"></div>
    <h2 class="front-title">Stille Pfade im Nebel<br>der Ostseeküste</h2>
    <p class="front-subtitle">Geschichten von Fischern und Leuchttürmen</p>
  </section>
</div>
</body>
</html>
```